Trainingsplaner 2014_KV

We would like to design a planer for our actual workshops. The planer should be for the whole of 2014 - please have a look at the enclosed file (Training Agenda) where you can find more details.
You'll also find our actual KVR_Booklet_P1 (Trainingsprogram) to give you the idea about the style we are using. As well as R4 Seminarkalender (as an idea) and an excel file (Trainingagenda_2014) with the actual dates of the workshops. Please also note that when you have a workshop or an event taking more than one day, that you visualize it over two or more days in one mention.
The planer size should be A3 cross and we would need print files.
The matter is very urgent! for any other question please don't hesitate to contact me, with my best regards
Wilma
Target Market(s)
Hairdressers of any age, very visual driven people
Industry/Entity Type
Training
Requirements
Must have
- The planer has to be A3 cross, months (vertical) and days (horizontal) have a look at the samples.

```html
<!DOCTYPE html>
<html lang="de">
<head>
<meta charset="utf-8">
<title>Trainingsplaner 2014</title>
<link href="https://fonts.googleapis.com/css2?family=PT+Serif:wght@700&family=Arimo:wght@400;700&display=swap" rel="stylesheet">
<style>
:root{
  --teal:#3f8f7d;
  --ink:#1f1f1f;
  --navy:#2c2b6f;
  --green:#6ebf2e;
  --green-dark:#4d9a1c;
  --green-light:#eaf8d4;
  --petrol:#2f7f82;
  --line:#3a3a3a;
  --paper:#ffffff;
}
*{box-sizing:border-box;margin:0;padding:0}
html,body{width:1200px;height:849px;overflow:hidden;background:var(--paper)}
body{position:relative;font-family:"Arimo",Arial,sans-serif;color:var(--ink)}
.header-band{position:absolute;left:0;top:0}
.title{position:absolute;left:0;width:940px;top:6px;text-align:center;font-family:"PT Serif",Georgia,serif;font-weight:700;font-size:31px;color:#fff;letter-spacing:.5px}
.subtitle{position:absolute;left:0;width:940px;top:51px;text-align:center;font-family:"PT Serif",Georgia,serif;font-weight:400;font-size:18.5px;color:#fff}
.brand{position:absolute;left:935px;top:30px;display:flex;align-items:center;gap:10px;font-family:"PT Serif",Georgia,serif;font-weight:700;font-size:25px;color:#2a2a2a;letter-spacing:1px}
.brand .dot{width:22px;height:22px;border-radius:50%;background:#c8202f}
.backdrop{position:absolute;left:107px;top:117px;width:1060px;height:694px;
  background:radial-gradient(ellipse at 25% 45%,rgba(150,110,95,.16),transparent 45%),
             radial-gradient(ellipse at 85% 40%,rgba(160,140,130,.18),transparent 40%),
             radial-gradient(ellipse at 60% 70%,rgba(190,160,150,.12),transparent 45%)}
.planner{position:absolute;left:23px;top:96px;width:1144px}
.row{display:grid;grid-template-columns:84px repeat(31,1fr)}
.days{height:21px}
.days span{font-weight:700;font-size:14px;color:var(--navy);text-align:center;line-height:21px}
.month{height:57.85px;border-top:1px solid var(--line)}
.month:last-child{border-bottom:1px solid var(--line)}
.mname{border-left:1px solid var(--line);border-right:1px solid var(--line);background:#fff;color:var(--navy);font-weight:700;font-size:14px;text-align:center;display:flex;flex-direction:column;justify-content:center;line-height:1.3}
.mname b{font-size:15px}
.month i,.month b.ev{font-style:normal;font-size:13px;text-align:center;border-right:1px solid var(--line);padding-top:2px;line-height:14px;overflow:hidden;position:relative}
.month i{background:rgba(255,255,255,.55)}
.month i.w{background:radial-gradient(circle at 50% 58%,var(--green-light) 0,#b6e07a 35%,var(--green) 75%,var(--green-dark) 100%);border-right-color:#fff}
.month i small{display:block;font-size:4.5px;line-height:5.5px;margin-top:2px;color:#333}
.month b.ev{font-weight:400;background:var(--paper);padding:2px}
.ev .box{display:block;height:100%;background:linear-gradient(180deg,var(--green) 0,#7cc93a 100%);color:#fff;padding-top:1px}
.ev .dl{display:flex;justify-content:space-around;font-size:13px;line-height:14px}
.ev em{display:block;font-style:normal;font-weight:700;font-size:5px;line-height:6px;margin-top:6px;padding:0 1px}
.ev .sub{display:block;position:absolute;right:2px;bottom:2px;width:32px;height:18px;background:var(--petrol);color:#fff;font-weight:700;font-size:4.5px;line-height:5.5px;padding-top:3px}
.ev .sub.dark{background:#2f7d33}
.footnote{position:absolute;left:24px;top:815px;font-size:10px;color:#222}
</style>
</head>
<body>
<svg class="header-band" width="1200" height="92" viewBox="0 0 1200 92" aria-hidden="true">
  <polygon points="0,0 905,0 840,88 0,88" fill="var(--teal)"/>
  <polygon points="912,0 922,0 857,88 847,88" fill="var(--teal)" opacity=".55"/>
  <polygon points="928,0 934,0 869,88 863,88" fill="var(--teal)" opacity=".3"/>
</svg>
<h1 class="title">TRAININGSPLANER 2014</h1>
<p class="subtitle">Wir freuen uns über Ihre Anmeldung auf www.karlvoss-academy.ch oder 043 555 12 34.</p>
<div class="brand"><span class="dot"></span>KARL VOSS</div>

<div class="backdrop" role="img" aria-label="Faint background photographs of styled hair models"></div>

<div class="planner">
  <div class="row days"><span></span><span>1</span><span>2</span><span>3</span><span>4</span><span>5</span><span>6</span><span>7</span><span>8</span><span>9</span><span>10</span><span>11</span><span>12</span><span>13</span><span>14</span><span>15</span><span>16</span><span>17</span><span>18</span><span>19</span><span>20</span><span>21</span><span>22</span><span>23</span><span>24</span><span>25</span><span>26</span><span>27</span><span>28</span><span>29</span><span>30</span><span>31</span></div>

  <div class="row month"><div class="mname"><b>1</b>Januar</div>
    <i>Mi<small>Neujahr</small></i><i>Do</i><i>Fr</i><i class="w">Sa</i><i class="w">So</i><i>Mo<small>Hl. Drei Könige</small></i><i>Di</i><i>Mi</i><i>Do</i><i>Fr</i><i class="w">Sa</i><i class="w">So</i><i>Mo</i><i>Di</i><i>Mi</i><i>Do</i><i>Fr</i><i class="w">Sa</i><i class="w">So</i>
    <b class="ev"><span class="box"><span class="dl">Mo</span><em>Principles of coloring</em></span></b>
    <i>Di</i><i>Mi</i><i>Do</i><i>Fr</i><i class="w">Sa</i><i class="w">So</i><i>Mo</i><i>Di</i><i>Mi</i><i>Do</i><i>Fr</i>
  </div>

  <div class="row month"><div class="mname"><b>2</b>Februar</div>
    <i class="w">Sa</i><i class="w">So</i>
    <b class="ev"><span class="box"><span class="dl">Mo</span><em>Collection Cut &amp; Color Spring 2014</em></span></b>
    <i>Di</i><i>Mi</i><i>Do</i><i>Fr</i><i class="w">Sa</i>
    <b class="ev"><span class="box"><span class="dl">So</span><em>Updo Session Petit Sac</em></span></b>
    <b class="ev"><span class="box"><span class="dl">Mo</span><em>Principles of Texture</em></span></b>
    <i>Di</i><i>Mi</i><i>Do</i><i>Fr<small>Valentinstag</small></i><i class="w">Sa</i><i class="w">So</i>
    <b class="ev"><span class="box"><span class="dl">Mo</span><em>Principles of coloring</em></span></b>
    <i>Di</i><i>Mi</i><i>Do</i><i>Fr</i><i class="w">Sa</i>
    <b class="ev"><span class="box"><span class="dl">So</span><em>Glowline Professional Stylist</em></span></b>
    <i>Mo</i><i>Di</i><i>Mi</i><i>Do</i><i>Fr</i>
  </div>

  <div class="row month"><div class="mname"><b>3</b>März</div>
    <i class="w">Sa</i><i class="w">So</i>
    <b class="ev"><span class="box"><span class="dl">Mo</span><em>Principles of coloring</em></span></b>
    <i>Di</i><i>Mi<small>Aschermittwoch</small></i><i>Do</i><i>Fr</i><i class="w">Sa</i>
    <b class="ev" style="grid-column:span 2"><span class="box"><span class="dl"><span>So</span><span>Mo</span></span><em>Long Hair Lover with Lena Morell</em></span></b>
    <i>Di</i><i>Mi</i><i>Do</i><i>Fr</i><i class="w">Sa</i><i class="w">So</i>
    <b class="ev"><span class="box"><span class="dl">Mo</span><em>Principles of Haircutting</em></span></b>
    <i>Di</i><i>Mi</i><i>Do</i><i>Fr</i>
    <b class="ev" style="grid-column:span 2"><span class="box"><span class="dl"><span>Sa</span><span>So</span></span><em>Hair Expo, Düsseldorf</em></span></b>
    <b class="ev"><span class="box"><span class="dl">Mo</span><em>Glowline Professional Stylist</em></span></b>
    <i>Di</i><i>Mi</i><i>Do</i><i>Fr</i><i class="w">Sa</i><i class="w">So</i>
    <b class="ev"><span class="box"><span class="dl">Mo</span><em>Style List</em></span></b>
  </div>

  <div class="row month"><div class="mname"><b>4</b>April</div>
    <i>Di</i><i>Mi</i><i>Do</i>
    <b class="ev" style="grid-column:span 4"><span class="box"><span class="dl"><span>Fr</span><span>Sa</span><span>So</span><span>Mo</span></span><em>Beautyfair, Bologna</em></span><span class="sub">Principles of coloring</span></b>
    <i>Di</i><i>Mi</i><i>Do</i><i>Fr</i><i class="w">Sa</i><i class="w">So</i>
    <b class="ev"><span class="box"><span class="dl">Mo</span><em>Ready for Short Hair</em></span></b>
    <i>Di</i><i>Mi</i><i>Do</i><i>Fr<small>Karfreitag</small></i><i class="w">Sa</i><i class="w">So<small>Ostern</small></i><i>Mo<small>Ostermontag</small></i><i>Di</i><i>Mi</i><i>Do</i><i>Fr</i><i class="w">Sa</i><i class="w">So</i><i>Mo</i><i>Di</i><i>Mi</i>
  </div>

  <div class="row month"><div class="mname"><b>5</b>Mai</div>
    <i>Do<small>Tag der Arbeit</small></i><i>Fr</i><i class="w">Sa</i><i class="w">So</i>
    <b class="ev"><span class="box"><span class="dl">Mo</span><em>Principles of coloring</em></span></b>
    <i>Di</i><i>Mi</i><i>Do</i><i>Fr</i><i class="w">Sa</i><i class="w">So</i>
    <b class="ev"><span class="box"><span class="dl">Mo</span><em>Ready for Curls</em></span></b>
    <i>Di</i><i>Mi</i><i>Do</i><i>Fr</i><i class="w">Sa</i><i class="w">So</i>
    <b class="ev"><span class="box"><span class="dl">Mo</span><em>Principles of Texture</em></span></b>
    <i>Di</i><i>Mi</i><i>Do</i><i>Fr</i><i class="w">Sa</i><i class="w">So</i>
    <b class="ev"><span class="box"><span class="dl">Mo</span><em>Advanced 10</em></span></b>
    <i>Di</i><i>Mi</i><i>Do<small>Christi Himmelfahrt</small></i><i>Fr</i><i class="w">Sa</i>
  </div>

  <div class="row month"><div class="mname"><b>6</b>Juni</div>
    <i class="w">So</i>
    <b class="ev"><span class="box"><span class="dl">Mo</span><em>Glowline Collection Red Carpet</em></span></b>
    <i>Di</i><i>Mi</i><i>Do</i><i>Fr</i><i class="w">Sa</i><i class="w">So<small>Pfingsten</small></i><i>Mo<small>Pfingstmontag</small></i><i>Di</i><i>Mi</i><i>Do</i><i>Fr</i><i class="w">Sa</i><i class="w">So</i>
    <b class="ev"><span class="box"><span class="dl">Mo</span><em>Principles of coloring</em></span></b>
    <i>Di</i><i>Mi</i><i>Do<small>Fronleichnam</small></i><i>Fr</i><i class="w">Sa</i><i class="w">So</i>
    <b class="ev"><span class="box"><span class="dl">Mo</span><em>Principles of styling</em></span></b>
    <i>Di</i><i>Mi</i><i>Do</i><i>Fr</i><i class="w">Sa</i><i class="w">So</i><i>Mo</i>
  </div>

  <div class="row month"><div class="mname"><b>7</b>Juli</div>
    <i>Di</i><i>Mi</i><i>Do</i><i>Fr</i><i class="w">Sa</i><i class="w">So</i>
    <b class="ev"><span class="box"><span class="dl">Mo</span><em>Principles of coloring</em></span></b>
    <i>Di</i><i>Mi</i><i>Do</i><i>Fr</i><i class="w">Sa</i><i class="w">So</i>
    <b class="ev"><span class="box"><span class="dl">Mo</span><em>Ready for Curls</em></span></b>
    <i>Di</i><i>Mi</i><i>Do</i><i>Fr</i><i class="w">Sa</i><i class="w">So</i>
    <b class="ev"><span class="box"><span class="dl">Mo</span><em>Glowline Professional Stylist</em></span></b>
    <i>Di</i><i>Mi</i><i>Do</i><i>Fr</i><i class="w">Sa</i><i class="w">So</i><i>Mo</i><i>Di</i><i>Mi</i><i>Do</i>
  </div>

  <div class="row month"><div class="mname"><b>8</b>August</div>
    <i>Fr<small>Nationalfeiertag</small></i><i class="w">Sa</i><i class="w">So</i>
    <b class="ev" style="grid-column:span 2"><span class="box"><span class="dl"><span>Mo</span><span>Di</span></span><em>The Stylist Summit Las Vegas</em></span></b>
    <i>Mi</i><i>Do</i><i>Fr</i><i class="w">Sa</i><i class="w">So</i>
    <b class="ev"><span class="box"><span class="dl">Mo</span><em>Principles of styling</em></span></b>
    <i>Di</i><i>Mi</i><i>Do</i><i>Fr<small>Mariä Himmelfahrt</small></i><i class="w">Sa</i><i class="w">So</i>
    <b class="ev"><span class="box"><span class="dl">Mo</span><em>Principles of Texture</em></span></b>
    <i>Di</i><i>Mi</i><i>Do</i><i>Fr</i><i class="w">Sa</i>
    <b class="ev"><span class="box"><span class="dl">So</span><em>Glowline Collection</em></span></b>
    <i>Mo</i><i>Di</i><i>Mi</i><i>Do</i><i>Fr</i><i class="w">Sa</i><i class="w">So</i>
  </div>

  <div class="row month"><div class="mname"><b>9</b>September</div>
    <b class="ev"><span class="box"><span class="dl">Mo</span><em>Cut &amp; Color Fall 2014</em></span><span class="sub">Balm Love</span></b>
    <i>Di</i><i>Mi</i><i>Do</i><i>Fr</i><i class="w">Sa</i><i class="w">So</i>
    <b class="ev"><span class="box"><span class="dl">Mo</span><em>Principles of coloring</em></span></b>
    <i>Di</i><i>Mi</i><i>Do</i><i>Fr</i><i class="w">Sa</i><i class="w">So</i>
    <b class="ev"><span class="box"><span class="dl">Mo</span><em>Principles of Haircutting</em></span></b>
    <i>Di</i><i>Mi</i><i>Do</i><i>Fr</i><i class="w">Sa</i><i class="w">So</i>
    <b class="ev"><span class="box"><span class="dl">Mo</span><em>Principles of Styling</em></span></b>
    <i>Di</i><i>Mi</i><i>Do</i><i>Fr</i><i class="w">Sa</i><i class="w">So</i><i>Mo</i><i>Di</i>
  </div>

  <div class="row month"><div class="mname"><b>10</b>Oktober</div>
    <i>Mi</i><i>Do</i><i>Fr<small>Tag d. Dt. Einheit</small></i><i class="w">Sa</i><i class="w">So</i>
    <b class="ev"><span class="box"><span class="dl">Mo</span><em>Principles of coloring</em></span></b>
    <i>Di</i><i>Mi</i><i>Do</i><i>Fr</i>
    <b class="ev" style="grid-column:span 3"><span class="box"><span class="dl"><span>Sa</span><span>So</span><span>Mo</span></span><em>Salon Forum, London</em></span><span class="sub dark">Ready for Short Hair</span></b>
    <i>Di</i><i>Mi</i><i>Do</i><i>Fr</i><i class="w">Sa</i><i class="w">So</i>
    <b class="ev"><span class="box"><span class="dl">Mo</span><em>Workshop Day</em></span></b>
    <i>Di</i><i>Mi</i><i>Do</i><i>Fr</i><i class="w">Sa</i>
    <b class="ev" style="grid-column:span 2"><span class="box"><span class="dl"><span>So</span><span>Mo</span></span><em>Haarmarathon, Meisterschneiden</em></span></b>
    <i>Di</i><i>Mi</i><i>Do</i><i>Fr<small>Reformationstag Halloween</small></i>
  </div>

  <div class="row month"><div class="mname"><b>11</b>November</div>
    <i class="w">Sa<small>Allerheiligen</small></i><i class="w">So</i>
    <b class="ev"><span class="box"><span class="dl">Mo</span><em>Principles of coloring</em></span></b>
    <i>Di</i><i>Mi</i><i>Do</i><i>Fr</i><i class="w">Sa</i><i class="w">So</i><i>Mo</i><i>Di</i><i>Mi</i><i>Do</i><i>Fr</i><i class="w">Sa</i><i class="w">So</i>
    <b class="ev"><span class="box"><span class="dl">Mo</span><em>Glowline Professional Stylist</em></span></b>
    <i>Di</i><i>Mi<small>Buß- und Bettag</small></i><i>Do</i><i>Fr</i><i class="w">Sa</i><i class="w">So<small>Totensonntag</small></i>
    <b class="ev"><span class="box"><span class="dl">Mo</span><em>Holiday Longhair Collection</em></span></b>
    <i>Di</i><i>Mi</i><i>Do</i><i>Fr</i><i class="w">Sa</i><i class="w">So</i>
  </div>

  <div class="row month"><div class="mname"><b>12</b>Dezember</div>
    <b class="ev"><span class="box"><span class="dl">Mo</span><em>Principles of Styling</em></span></b>
    <i>Di</i><i>Mi</i><i>Do</i><i>Fr</i><i class="w">Sa<small>Nikolaus</small></i><i class="w">So</i>
    <b class="ev"><span class="box"><span class="dl">Mo</span><em>Principles of Coloring</em></span></b>
    <i>Di</i><i>Mi</i><i>Do</i><i>Fr</i><i class="w">Sa</i><i class="w">So</i><i>Mo</i><i>Di</i><i>Mi</i><i>Do</i><i>Fr</i><i class="w">Sa</i><i class="w">So</i><i>Mo</i><i>Di</i><i>Mi<small>Heiligabend</small></i><i>Do<small>1. Weihnachtstag</small></i><i>Fr<small>2. Weihnachtstag</small></i><i class="w">Sa</i><i class="w">So</i><i>Mo</i><i>Di</i><i>Mi</i>
  </div>
</div>

<p class="footnote">Änderungen vorbehalten</p>
</body>
</html>
```